Merchandising Kaffeebohnen mit Firmen Branding
Zielgruppe
Willkommen bei KLV Talmetall, Ihrem internationalen Experten für smarte Recycling- und Verwertungslösungen in der Elektronikbranche. Wir steigern die nachhaltige und wirtschaftliche Performance Ihres Unternehmens mit maßgeschneiderten und CO2-reduzierenden Recyclinglösungen für Lötzinn und edelmetallhaltige Produktionsabfälle. Mit unserer proaktiven Beratung helfen wir Ihrem Unternehmen, nicht nur umweltfreundlich zu agieren, sondern leisten einen messbaren Beitrag für eine zukunftsorientierte Marktpositionierung!
Aufgabenstellung
Modern & schlicht
Wir haben eine Espresso Event und dazu unseren eigenen Kaffee und dafür benötigen wir ein Design.

```html
<!DOCTYPE html>
<html lang="en">
<head>
<meta charset="utf-8">
<title>KLV Talmetall Espresso – Packaging</title>
<link href="https://fonts.googleapis.com/css2?family=Barlow+Condensed:wght@300;400;500&family=Big+Shoulders+Display:wght@300&display=swap" rel="stylesheet">
<style>
:root{
  --backdrop:#f6efe4;
  --bag:#1d1e21;
  --bag-seal:#17181a;
  --gold:#c9ae78;
  --white:#ffffff;
  --line-grey:#8d8d90;
}
*{margin:0;padding:0;box-sizing:border-box}
html,body{width:1200px;height:1066px;overflow:hidden;background:var(--backdrop)}
body{position:relative;font-family:"Barlow Condensed",sans-serif;color:var(--white)}
.bag{position:absolute;top:122px;width:376px;height:820px;background:var(--bag);border-radius:14px;overflow:hidden}
.bag--front{left:190px}
.bag--back{left:623px}
.bag__seal{position:absolute;left:0;top:0;width:100%;height:72px;background:var(--bag-seal)}
.pattern{position:absolute}
.bag--front .pattern{left:0;top:98px;width:376px;height:560px;
  background:radial-gradient(ellipse at 70% 25%,rgba(220,220,225,.16),transparent 55%),radial-gradient(ellipse at 35% 70%,rgba(201,174,120,.18),transparent 60%)}
.bag--back .pattern{left:44px;top:183px;width:290px;height:335px;
  background:radial-gradient(ellipse at 65% 30%,rgba(220,220,225,.15),transparent 60%),radial-gradient(ellipse at 35% 72%,rgba(201,174,120,.17),transparent 62%)}
.brand{position:absolute;display:flex;align-items:center;gap:8px;font-weight:500;color:var(--white);letter-spacing:.04em;text-transform:uppercase}
.brand__mark{width:12px;height:12px;background:var(--white)}
.bag--front .brand{left:86px;top:424px;font-size:30px}
.bag--back .brand{left:58px;top:744px;font-size:19px}
.bag--back .brand__mark{width:9px;height:9px}
.product-name{position:absolute;left:64px;top:522px;font-family:"Big Shoulders Display",sans-serif;font-weight:300;font-size:164px;line-height:1;letter-spacing:.01em;transform:scaleX(.62);transform-origin:left top;white-space:nowrap}
.tagline{position:absolute;left:64px;top:688px;width:248px;font-size:19.5px;color:var(--gold);text-align:justify;text-align-last:justify;white-space:nowrap}
.roast{position:absolute;left:64px;top:718px;width:248px;height:44px;color:var(--gold);font-size:19px;line-height:19px}
.roast__label--light{position:absolute;left:0;top:2px}
.roast__label--deep{position:absolute;right:0;top:-2px;text-align:right}
.roast__dot{position:absolute;top:15px;width:15px;height:15px;border:1.3px solid var(--gold);border-radius:50%}
.roast__dot--active{background:var(--gold)}
.facts{position:absolute;left:52px;top:521px;font-size:12px;line-height:16px;font-weight:400}
.description{position:absolute;left:52px;top:561px;width:140px;font-size:9.6px;line-height:15.3px;color:var(--gold);font-weight:400}
.prep{position:absolute;left:212px;font-size:10px;font-weight:400}
.prep--grind{top:558px}
.prep--suits{top:586px}
.prep-icon{position:absolute;left:277px;width:34px;border:1px solid var(--gold);border-radius:3px;opacity:.7}
.prep-icon--grinder{top:540px;height:36px}
.prep-icon--moka{top:582px;height:33px}
.prep-icon--machine{top:626px;height:34px}
.recycle{position:absolute;left:191px;top:683px;width:29px;height:29px;border-radius:50%;background:var(--white)}
.weight{position:absolute;left:236px;top:674px;font-size:42px;font-weight:400;line-height:1}
.address{position:absolute;right:71px;top:735px;font-size:9.2px;line-height:10.6px;text-align:right;color:var(--gold);font-weight:300;font-style:normal}
</style>
</head>
<body>
<section class="bag bag--front">
  <div class="bag__seal"></div>
  <div class="pattern" role="img" aria-label="Interlocking hexagonal line pattern in white and gold"></div>
  <div class="brand"><span class="brand__mark"></span>KLV Group</div>
  <h1 class="product-name">ESPRESSO</h1>
  <p class="tagline">100% arabica whole coffee beans</p>
  <div class="roast">
    <span class="roast__label--light">light<br>roast</span>
    <span class="roast__dot" style="left:53px"></span>
    <span class="roast__dot" style="left:84px"></span>
    <span class="roast__dot" style="left:116px"></span>
    <span class="roast__dot roast__dot--active" style="left:148px"></span>
    <span class="roast__dot" style="left:179px"></span>
    <span class="roast__label--deep">deep<br>roast</span>
  </div>
</section>

<section class="bag bag--back">
  <div class="bag__seal"></div>
  <div class="pattern" role="img" aria-label="Interlocking hexagonal line pattern in white and gold"></div>
  <p class="facts">100% arabica<br>whole coffee beans</p>
  <p class="description">Lorem ipsum dolor sit amet, consectetuer adipiscing elit, sed diam nonummy nibh euismod tincidunt ut laoreet dolore magna aliquam erat volutpat. Ut wisi enim ad minim veniam, quis nostrud exerci tation</p>
  <p class="prep prep--grind">grind grade II</p>
  <p class="prep prep--suits">suitable for</p>
  <div class="prep-icon prep-icon--grinder" role="img" aria-label="Coffee grinder icon"></div>
  <div class="prep-icon prep-icon--moka" role="img" aria-label="Moka pot icon"></div>
  <div class="prep-icon prep-icon--machine" role="img" aria-label="Espresso machine icon"></div>
  <div class="recycle" role="img" aria-label="Recycling badge"></div>
  <p class="weight">250g</p>
  <div class="brand"><span class="brand__mark"></span>KLV Talmetall</div>
  <address class="address">KLV Talmetall GmbH<br>Birkenweg 12<br>45100 Talstadt</address>
</section>
</body>
</html>
```